The Corliss Lane Stories

The book is written by the 2nd oldest of 14 children who grew up in a 900 sq ft home, under the overtly line, raised by an awesome loving mother and a tough, mostly wrong father. The house was located at 14 3 North Corliss Lane. The stories took place in the 1950s. It’s a collection of 25 true stories ranging from funny to tragic. But they are stories of beautiful redemption, with all 14 becoming very successful. The cover should have a nostalgic look. Here are a few chapters.

Target Market(s)

General audience 18+

Industry/Entity Type

None. Family

Font styles to use
Serif
Sans Serif
Decorative
Script

Requirements
Should not have
• Nothing modern or contemporary

```html
<!DOCTYPE html>
<html lang="en">
<head>
<meta charset="utf-8">
<title>The Corliss Lane Stories – Book Cover Spread</title>
<link rel="stylesheet" href="https://fonts.googleapis.com/css2?family=Cinzel:wght@400;600;700&family=EB+Garamond:wght@400;500;600&display=swap">
<style>
  :root {
    --page-bg: #ffffff;
    --back-teal: #6db8ab;
    --spine-teal: #167178;
    --cream: #f4edc9;
    --photo-light: #6fa89c;
    --photo-mid: #4f8a80;
    --photo-dark: #1f4a45;
  }
  * { margin: 0; padding: 0; box-sizing: border-box; }
  html, body {
    width: 960px; height: 1200px; overflow: hidden;
    background: var(--page-bg);
  }
  .canvas {
    position: relative; width: 960px; height: 1200px;
  }
  .cover-spread {
    position: absolute; left: 40px; top: 287px;
    width: 880px; height: 627px;
    display: flex;
  }
  .back-cover {
    width: 410px; height: 100%;
    background: var(--back-teal);
    color: var(--cream);
    padding: 0 18px;
    position: relative;
  }
  .back-title {
    position: absolute; left: 0; right: 0; top: 82px;
    text-align: center;
    font-family: 'Cinzel', serif; font-weight: 600;
    font-size: 25px; letter-spacing: 0.3px;
  }
  .section-heading {
    font-family: 'EB Garamond', serif; font-weight: 600;
    text-align: center; text-transform: uppercase;
    font-size: 17px; margin-bottom: 2px;
  }
  .summary { position: absolute; left: 18px; right: 18px; top: 198px; }
  .summary p {
    font-family: 'EB Garamond', serif;
    font-size: 15px; line-height: 17.2px; text-align: justify;
  }
  .bio { position: absolute; left: 18px; right: 18px; top: 397px; }
  .bio p {
    font-family: 'EB Garamond', serif;
    font-size: 12.4px; line-height: 13.4px; text-align: justify;
  }
  .spine {
    width: 59px; height: 100%;
    background: var(--spine-teal);
    position: relative;
  }
  .spine-title {
    position: absolute; left: 50%; top: 168px;
    transform-origin: 0 0;
    transform: rotate(90deg) translate(0, -50%);
    white-space: nowrap;
    font-family: 'Cinzel', serif; font-weight: 600;
    font-size: 25px; color: var(--cream);
    width: 390px; text-align: center; margin-left: 1px;
  }
  .front-cover {
    width: 411px; height: 100%; position: relative; overflow: hidden;
  }
  .cover-photo {
    position: absolute; inset: 0;
    background:
      radial-gradient(ellipse 60% 40% at 80% 15%, rgba(31,74,69,0.85), rgba(31,74,69,0) 70%),
      linear-gradient(90deg, rgba(0,0,0,0) 70%, rgba(20,50,46,0.7) 100%),
      linear-gradient(180deg, var(--photo-light) 0%, var(--photo-mid) 50%, #3f7a70 75%, #4d8a7e 100%);
  }
  .front-title {
    position: absolute; left: 0; right: 0; top: 412px;
    text-align: center;
    font-family: 'Cinzel', serif; font-weight: 700;
    font-size: 58px; line-height: 67px;
    color: var(--cream);
    padding-left: 8px;
  }
</style>
</head>
<body>
<main class="canvas">
  <section class="cover-spread">
    <article class="back-cover">
      <h2 class="back-title">The Corliss Lane Stories</h2>
      <div class="summary">
        <h3 class="section-heading">Summary</h3>
        <p>Lorem ipsum dolor sit amet, consectetur adipiscing elit, sed do eiusmod tempor incididunt ut labore et dolore magna aliqua. Ut enim ad minim veniam, quis nostrud exercitation ullamco laboris nisi ut aliquip ex ea commodo consequat. Duis aute irure dolor in reprehenderit in voluptate velit esse cillum dolore eu fugiat nulla pariatur. Excepteur sint occaecat cupidatat non proident, sunt in culpa qui officia deserunt mollit anim id est laborum.</p>
      </div>
      <div class="bio">
        <h3 class="section-heading">Bio:</h3>
        <p>Sed ut perspiciatis, unde omnis iste natus error sit voluptatem accusantium doloremque laudantium, totam rem aperiam eaque ipsa, quae ab illo inventore veritatis et quasi architecto beatae vitae dicta sunt, explicabo. Nemo enim ipsam voluptatem, quia voluptas sit, aspernatur aut odit aut fugit, sed quia consequuntur magni dolores eos, qui ratione voluptatem sequi nesciunt, neque porro quisquam est, qui dolorem ipsum, quia dolor sit amet consectetur adipisci[ng] velit, sed quia non numquam</p>
      </div>
    </article>
    <div class="spine">
      <span class="spine-title">The Corliss Lane Stories</span>
    </div>
    <article class="front-cover">
      <div class="cover-photo" role="img" aria-label="Teal-toned photograph of a small single-storey house with a gabled porch, lawn in front and trees behind"></div>
      <h1 class="front-title">The Corliss<br>Lane<br>Stories</h1>
    </article>
  </section>
</main>
</body>
</html>
```